TideMill Coatings website development for protective coatings manufacturer

We require a website for a new company which manufacturers protective coatings for automotive and industrial applications. We have a new logo which can be used and will be uploaded for inclusion on the website. There should be the following pages:
Home
About us
Products
Distribution
Contact us
There will be 10 products with downloadable pdf files TDS and MSDS.
Target Market(s)
Automotive and industrial coatings
Industry/Entity Type
Protective Coatings manufacturing
Coding
Coded - Design and coding required
Font styles to use
Sans Serif
Requirements
Must have
- Nice and clear images related to the target market

```html
<!DOCTYPE html>
<html lang="en">
<head>
<meta charset="utf-8">
<title>TideMill Coatings</title>
<link href="https://fonts.googleapis.com/css2?family=Ubuntu:wght@400;500;700&family=Open+Sans:wght@400;600;700&display=swap" rel="stylesheet">
<style>
:root{
  --navy:#1f3f75;
  --navy-deep:#1b3560;
  --ink:#1c2436;
  --topbar:#1d2538;
  --testi:#0f2b4d;
  --cyan:#2fb3e3;
  --text:#5d6472;
  --muted:#8a909c;
  --light:#f4f4f5;
  --white:#fff;
}
*{box-sizing:border-box;margin:0;padding:0}
html,body{width:1200px;height:4754px;overflow:hidden}
body{position:relative;font-family:"Open Sans",sans-serif;color:var(--text);background:var(--white)}
.abs{position:absolute}
h1,h2,h3,h4,.head{font-family:"Ubuntu",sans-serif}
.btn{position:absolute;display:flex;align-items:center;justify-content:center;gap:12px;font-family:"Ubuntu",sans-serif;font-weight:500;color:#fff;background:var(--cyan);font-size:16px}
.label{position:absolute;font-size:12px;color:var(--cyan);letter-spacing:.3px;text-transform:uppercase;border-bottom:1px solid var(--cyan);padding-bottom:3px}
.photo{position:absolute}

/* top bar */
.topbar{left:0;top:0;width:1200px;height:44px;background:var(--topbar);color:#c9cdd6;font-size:14px}
.topbar span{position:absolute;top:13px}
.topbar .soc{position:absolute;top:17px;width:10px;height:10px;background:#c9cdd6;border-radius:2px}
.topbar .sep{position:absolute;top:12px;width:1px;height:20px;background:#4a5266}

/* header */
.brand{position:absolute;font-family:"Ubuntu",sans-serif;font-weight:700;color:var(--navy);font-size:24px;line-height:1}
.hinfo{position:absolute;font-size:14px;color:var(--ink)}
.hinfo small{display:block;font-size:13px;color:var(--muted);margin-top:4px}
.nav{left:78px;top:153px;width:987px;height:68px;background:#fff;z-index:3}
.nav a{position:absolute;top:26px;font-size:14px;color:#687080;text-decoration:none}
.nav a.on{color:var(--navy);font-weight:600}

/* hero */
.hero-title{left:100px;top:440px;font-size:96px;font-weight:700;color:#fff;line-height:1}
.hero-tag{left:100px;top:400px;width:268px;height:41px;background:var(--navy);border-left:4px solid var(--cyan);color:#fff;font-family:"Ubuntu";font-weight:500;font-size:21px;padding:7px 0 0 18px}
.hero-text{left:100px;top:558px;width:460px;font-size:16px;line-height:26px;color:#e6e9ef}

/* sections */
.sec-title{position:absolute;font-family:"Ubuntu",sans-serif;font-weight:500;color:var(--navy);font-size:40px}
.para{position:absolute;font-size:13px;line-height:21px;color:#808693}
.prod{position:absolute;top:1684px;width:317px;height:354px;border-radius:4px;overflow:hidden}
.prod h3{position:absolute;left:28px;top:228px;color:#fff;font-weight:500;font-size:25px}
.prod .go{position:absolute;left:28px;top:282px;width:48px;height:48px;border-radius:50%;background:rgba(255,255,255,.25);display:flex;align-items:center;justify-content:center}
.feat{position:absolute;top:2237px;width:233px;height:360px;background:#fff;box-shadow:0 4px 18px rgba(20,40,80,.12);text-align:center}
.feat h4{margin-top:100px;color:var(--navy);font-weight:500;font-size:19px}
.feat p{margin:14px 28px 0;font-size:14px;line-height:25px;color:#6a7180}
.feat .more{margin-top:24px;font-family:"Ubuntu";font-weight:500;font-size:14px;color:var(--navy)}
.feat svg.ic{position:absolute;left:96px;top:36px}
.why h4{font-family:"Ubuntu";font-weight:500;font-size:20px;color:var(--navy)}
.why p{font-size:13px;line-height:21px;color:#838996;margin-top:6px}
.why{position:absolute}
.wic{position:absolute;width:74px;height:74px;border-radius:50%;background:#fff;box-shadow:0 3px 14px rgba(20,40,80,.12);display:flex;align-items:center;justify-content:center}
.tcard{position:absolute;top:3461px;width:322px;height:222px;background:#1b3a60;border-radius:4px;padding:0 30px}
.tcard .q{position:absolute;left:145px;top:-14px;font-family:"Ubuntu";font-weight:700;color:var(--cyan);font-size:60px;line-height:1}
.tcard p{margin-top:40px;font-size:13.5px;line-height:23px;color:#dbe2ec}
.tcard .who{position:absolute;left:30px;top:165px;display:flex;gap:14px;align-items:center}
.tcard .av{width:46px;height:46px;border-radius:50%;background:linear-gradient(#c9a98c,#6e5a4c)}
.tcard .nm{font-family:"Ubuntu";color:#fff;font-size:16px}
.tcard .nm small{display:block;color:#8b9bb2;font-size:15px}
.citem{position:absolute;left:100px;display:flex;gap:22px;align-items:center}
.citem b{display:block;font-size:13px;color:var(--ink);font-weight:700}
.citem span{font-size:13px;color:#7f8592}
.field{position:absolute;border:1px solid #c6cbd3;border-radius:22px;font-size:13px;color:#9aa0aa;padding-left:26px;display:flex;align-items:center}
.flabel{position:absolute;font-size:13px;font-weight:700;color:var(--ink)}
.foot-nav a{position:absolute;top:4633px;font-size:14px;color:#fff;text-decoration:none}
.fcontact{position:absolute;top:4534px;display:flex;gap:12px;color:#fff;font-size:14px;line-height:19px}
.fsq{position:absolute;top:4710px;width:24px;height:24px;border:1px solid #fff}
.fsq i{position:absolute;left:7px;top:7px;width:8px;height:8px;background:#fff}
.foot-brand{position:absolute;left:182px;top:4516px;display:flex;align-items:center;gap:12px;font-family:"Ubuntu",sans-serif;font-weight:700;color:#fff;font-size:28px;line-height:31px;white-space:nowrap}
</style>
</head>
<body>

<!-- Top bar -->
<div class="abs topbar">
  <svg class="abs" style="left:78px;top:15px" width="14" height="14" viewBox="0 0 14 14"><circle cx="7" cy="7" r="6" fill="none" stroke="#2fb3e3" stroke-width="1.5"/><path d="M7 3.5V7l2.5 1.5" stroke="#2fb3e3" stroke-width="1.5" fill="none"/></svg>
  <span style="left:101px">Mon-Sat: 09am to 07:30pm</span>
  <svg class="abs" style="left:324px;top:17px" width="14" height="10" viewBox="0 0 14 10"><rect x=".75" y=".75" width="12.5" height="8.5" fill="none" stroke="#2fb3e3" stroke-width="1.5"/><path d="M1 1l6 4.5L13 1" stroke="#2fb3e3" stroke-width="1.5" fill="none"/></svg>
  <span style="left:348px">hello@tidemill.example</span>
  <i class="sep" style="left:870px"></i>
  <span style="left:886px">Faqs</span>
  <i class="sep" style="left:937px"></i>
  <span style="left:953px">Pricing</span>
  <i class="sep" style="left:1021px"></i>
  <i class="soc" style="left:1037px"></i><i class="soc" style="left:1063px"></i><i class="soc" style="left:1092px"></i><i class="soc" style="left:1122px"></i>
</div>

<!-- Header -->
<div class="brand" style="left:85px;top:88px;display:flex;align-items:center;gap:8px"><i style="width:16px;height:16px;background:var(--navy);display:block"></i>TideMill Coatings</div>
<svg class="abs" style="left:362px;top:80px" width="34" height="34" viewBox="0 0 34 34"><path d="M4 14c0-5 26-5 26 0l-4 3-4-3v-2H12v2l-4 3z" fill="none" stroke="#1f3f75" stroke-width="2"/><rect x="8" y="17" width="18" height="13" rx="2" fill="none" stroke="#1f3f75" stroke-width="2"/><circle cx="17" cy="23" r="3" fill="#1f3f75"/></svg>
<div class="hinfo" style="left:411px;top:76px">+10-555-01-2400<small>Need help? Make a Call</small></div>
<svg class="abs" style="left:663px;top:80px" width="32" height="32" viewBox="0 0 32 32"><circle cx="16" cy="16" r="13" fill="none" stroke="#1f3f75" stroke-width="2"/><path d="M3 16h26M16 3c-6 7-6 19 0 26M16 3c6 7 6 19 0 26" fill="none" stroke="#1f3f75" stroke-width="1.6"/></svg>
<div class="hinfo" style="left:710px;top:76px">Australia<small>212A Someplace somewhere</small></div>
<div class="btn" style="left:956px;top:76px;width:181px;height:46px;background:var(--navy);border-radius:3px;font-size:14px">Free Estimate
  <svg width="18" height="18" viewBox="0 0 18 18"><circle cx="9" cy="9" r="8" fill="none" stroke="#fff" stroke-width="1.5"/><path d="M5 9h8M10 6l3 3-3 3" stroke="#fff" stroke-width="1.5" fill="none"/></svg></div>

<!-- Hero -->
<svg class="abs" style="left:0;top:153px" width="1200" height="770" viewBox="0 0 1200 770" role="img" aria-label="Technician in a white protective suit and respirator spray-painting in a workshop">
  <defs><linearGradient id="hg" x1="0" x2="1" y1="0" y2="1"><stop offset="0" stop-color="#3e444c"/><stop offset=".6" stop-color="#2c3036"/><stop offset="1" stop-color="#4a4f55"/></linearGradient></defs>
  <polygon points="0,0 1200,0 1200,604 600,761 0,604" fill="url(#hg)"/>
  <polyline points="0,604 600,761 1200,604" fill="none" stroke="#2fb3e3" stroke-width="6"/>
</svg>
<div class="abs nav">
  <a class="on" style="left:86px">Home</a><a style="left:198px">About Us</a><a style="left:310px">Production</a><a style="left:448px">Distribution</a><a style="left:592px">Gallery</a><a style="left:692px">Contact Us</a>
</div>
<div class="abs" style="left:1065px;top:153px;width:72px;height:68px;background:var(--navy);z-index:3;display:flex;align-items:center;justify-content:center">
  <svg width="34" height="34" viewBox="0 0 24 24"><path d="M5 3h4l2 5-2.5 1.5a11 11 0 0 0 6 6L16 13l5 2v4a2 2 0 0 1-2 2A16 16 0 0 1 3 5a2 2 0 0 1 2-2z" fill="none" stroke="#6fc8ef" stroke-width="1.5"/></svg></div>
<div class="abs hero-tag">We are leaders in</div>
<h1 class="abs hero-title">Coatings</h1>
<p class="abs hero-text">Lorem ipsum dolor sit amet, consectetur adipiscing elit, sed do eiusmod tempor i</p>
<div class="btn" style="left:100px;top:640px;width:175px;height:50px;font-size:15px">Read More</div>

<!-- About -->
<div class="photo" role="img" aria-label="Smiling worker in white coveralls holding a respirator mask" style="left:89px;top:967px;width:234px;height:418px;background:linear-gradient(#e6e8ec,#b9c1cc)"></div>
<div class="photo" role="img" aria-label="Close-up of a polishing machine buffing a car surface" style="left:342px;top:990px;width:234px;height:417px;background:linear-gradient(135deg,#2a2d31,#8b8e92 60%,#3a3d41)"></div>
<div class="abs" style="left:290px;top:1147px;width:80px;height:80px;border-radius:50%;background:var(--navy);border:4px solid #fff;display:flex;align-items:center;justify-content:center">
  <svg width="36" height="36" viewBox="0 0 36 36"><path d="M6 18a12 12 0 0 1 21-8M30 18a12 12 0 0 1-21 8" fill="none" stroke="#6fc8ef" stroke-width="2"/><path d="M18 11c-4 5-5 8-3 10s5 1 5-2-2-5-2-8z" fill="none" stroke="#6fc8ef" stroke-width="2"/></svg></div>
<div class="label" style="left:613px;top:977px">Who we are</div>
<h2 class="sec-title" style="left:613px;top:1012px;width:520px;line-height:51px;font-size:41px">Your Coating Solutions Partner</h2>
<div class="abs head" style="left:613px;top:1145px;font-size:21px;color:var(--ink);font-weight:500">Premium Quality, Lasting Durability</div>
<p class="para" style="left:613px;top:1187px;width:505px">Lorem ipsum dolor sit amet, consectetur adipiscing elit, sed do eiusmod temp or incididunt ut labore et dolore magna aliqua. Ut enim ad minim veniam, quis laboris nisi ut aliquip ex ea commodo consequat.</p>
<p class="para" style="left:613px;top:1263px;width:505px">Lorem ipsum dolor sit amet, consectetur adipiscing elit, sed do eiusmod temp or incididunt ut labore et dolore magna aliqua.</p>
<div class="btn" style="left:611px;top:1346px;width:155px;height:44px">Contact us
  <svg width="18" height="12" viewBox="0 0 18 12"><path d="M0 6h16M11 1l5 5-5 5" stroke="#fff" stroke-width="1.6" fill="none"/></svg></div>

<!-- Products -->
<div class="abs" style="left:0;top:1473px;width:1200px;height:650px;background:var(--light)"></div>
<div class="label" style="left:84px;top:1534px">Our products</div>
<h2 class="sec-title" style="left:84px;top:1567px">Coatings We Provide</h2>
<div class="prod" style="left:96px" role="img" aria-label="Spray booth with a worker coating industrial panels">
  <div style="position:absolute;inset:0;background:linear-gradient(#c7ccd3 0%,#8894a6 45%,#24467e 100%)"></div>
  <h3>Industrial</h3><div class="go"><svg width="16" height="12" viewBox="0 0 16 12"><path d="M0 6h14M9 1l5 5-5 5" stroke="#fff" stroke-width="1.5" fill="none"/></svg></div></div>
<div class="prod" style="left:441px" role="img" aria-label="Yellow cloth polishing a blue car body">
  <div style="position:absolute;inset:0;background:linear-gradient(#dfe3e8 0%,#5b77a4 45%,#1f3f75 100%)"></div>
  <h3>Automotive</h3><div class="go"><svg width="16" height="12" viewBox="0 0 16 12"><path d="M0 6h14M9 1l5 5-5 5" stroke="#fff" stroke-width="1.5" fill="none"/></svg></div></div>
<div class="prod" style="left:788px" role="img" aria-label="Gloved hand holding a spray gun in a booth">
  <div style="position:absolute;inset:0;background:linear-gradient(90deg,#2b5fb0 0%,#b7c2d2 55%,#e4e8ee 100%)"></div>
  <div style="position:absolute;inset:0;background:linear-gradient(rgba(31,63,117,0) 40%,#1f3f75 100%)"></div>
  <h3>Special Purpose</h3><div class="go"><svg width="16" height="12" viewBox="0 0 16 12"><path d="M0 6h14M9 1l5 5-5 5" stroke="#fff" stroke-width="1.5" fill="none"/></svg></div></div>

<!-- Leading provider -->
<div class="abs" style="left:0;top:2123px;width:1200px;height:388px;background:linear-gradient(var(--navy-deep),#224577)"></div>
<div class="abs" style="left:0;top:2511px;width:1200px;height:738px;background:var(--light)"></div>
<h2 class="abs" style="left:89px;top:2230px;font-size:41px;line-height:51px;color:#fff;font-weight:500">Leading<br>Coatings<br>Provider</h2>
<div class="btn" style="left:90px;top:2404px;width:156px;height:46px">Contact us
  <svg width="18" height="12" viewBox="0 0 18 12"><path d="M0 6h16M11 1l5 5-5 5" stroke="#fff" stroke-width="1.6" fill="none"/></svg></div>
<div class="feat" style="left:353px">
  <svg class="ic" width="40" height="40" viewBox="0 0 40 40"><circle cx="20" cy="13" r="7" fill="none" stroke="#2fb3e3" stroke-width="2"/><path d="M6 36c0-8 6-12 14-12s14 4 14 12z" fill="none" stroke="#1f3f75" stroke-width="2"/></svg>
  <h4>Professionalism</h4><p>Lorem ipsum dolor sit consectetur adipiscing elit, sed do eiusmod tempor incididunt</p><div class="more">Read More &nbsp;→</div></div>
<div class="feat" style="left:611px">
  <svg class="ic" width="40" height="40" viewBox="0 0 40 40"><circle cx="20" cy="22" r="15" fill="none" stroke="#1f3f75" stroke-width="2"/><path d="M20 22l7-7" stroke="#2fb3e3" stroke-width="2.5"/><circle cx="20" cy="22" r="2.5" fill="#2fb3e3"/></svg>
  <h4>Available 24/7</h4><p>Lorem ipsum dolor sit consectetur adipiscing elit, sed do eiusmod tempor incididunt</p><div class="more">Read More &nbsp;→</div></div>
<div class="feat" style="left:873px">
  <svg class="ic" width="40" height="40" viewBox="0 0 40 40"><path d="M16 6l10 6-8 14-10-6z" fill="none" stroke="#2fb3e3" stroke-width="2"/><path d="M6 36h28M10 30h20" stroke="#1f3f75" stroke-width="2"/></svg>
  <h4>High Quality</h4><p>Lorem ipsum dolor sit consectetur adipiscing elit, sed do eiusmod tempor incididunt</p><div class="more">Read More &nbsp;→</div></div>

<!-- Why choose us -->
<div class="label" style="left:543px;top:2656px">Why choose us</div>
<h2 class="sec-title" style="left:0;top:2690px;width:1200px;text-align:center">Why Choose Us</h2>
<svg class="abs" style="left:340px;top:2830px" width="520" height="320" viewBox="0 0 520 320"><path d="M55 30a250 250 0 0 0 0 250M465 30a250 250 0 0 1 0 250" fill="none" stroke="#cfd3da" stroke-width="2"/></svg>
<div class="abs" role="img" aria-label="Painter in protective suit and respirator aiming a spray gun" style="left:434px;top:2821px;width:332px;height:332px;border-radius:50%;background:radial-gradient(circle at 50% 40%,#e4e7ee,#5f6e93 70%,#3d4a70)"></div>
<div class="wic" style="left:356px;top:2825px"><svg width="34" height="34" viewBox="0 0 34 34"><circle cx="17" cy="11" r="5" fill="none" stroke="#1f3f75" stroke-width="1.8"/><circle cx="7" cy="15" r="3.5" fill="none" stroke="#2fb3e3" stroke-width="1.8"/><circle cx="27" cy="15" r="3.5" fill="none" stroke="#2fb3e3" stroke-width="1.8"/><path d="M9 29c0-6 4-9 8-9s8 3 8 9" fill="none" stroke="#1f3f75" stroke-width="1.8"/></svg></div>
<div class="wic" style="left:323px;top:2950px"><svg width="34" height="34" viewBox="0 0 34 34"><circle cx="17" cy="17" r="13" fill="none" stroke="#1f3f75" stroke-width="1.8"/><path d="M11 22c3-4 9-4 12 0M12 13h3M19 13h3" stroke="#1f3f75" stroke-width="1.8" fill="none"/></svg></div>
<div class="wic" style="left:356px;top:3075px"><svg width="34" height="34" viewBox="0 0 34 34"><path d="M6 17a11 11 0 0 1 19-7M28 17a11 11 0 0 1-19 7" fill="none" stroke="#1f3f75" stroke-width="1.8"/><path d="M17 11c-3 4-4 7-2 8s4 0 4-2-2-4-2-6z" fill="none" stroke="#2fb3e3" stroke-width="1.8"/></svg></div>
<div class="wic" style="left:766px;top:2825px"><svg width="34" height="34" viewBox="0 0 34 34"><path d="M13 5l9 5-7 12-9-5z" fill="none" stroke="#2fb3e3" stroke-width="1.8"/><path d="M5 29h24M9 24h16" stroke="#1f3f75" stroke-width="1.8"/></svg></div>
<div class="wic" style="left:799px;top:2950px"><svg width="34" height="34" viewBox="0 0 34 34"><path d="M17 4l4 8 9 1-6 6 2 9-9-4-9 4 2-9-6-6 9-1z" fill="none" stroke="#1f3f75" stroke-width="1.8"/></svg></div>
<div class="wic" style="left:766px;top:3075px"><svg width="34" height="34" viewBox="0 0 34 34"><circle cx="17" cy="17" r="5" fill="none" stroke="#2fb3e3" stroke-width="1.8"/><circle cx="17" cy="17" r="11" fill="none" stroke="#1f3f75" stroke-width="1.8" stroke-dasharray="5 3"/></svg></div>
<div class="why" style="left:148px;top:2830px;width:185px"><h4>Advanced Tech</h4><p>Lorem ipsum dolor sit amet, consectetur adipiscing</p></div>
<div class="why" style="left:117px;top:2955px;width:190px"><h4>Timely Delivery</h4><p>Lorem ipsum dolor sit amet, consectetur adipiscing</p></div>
<div class="why" style="left:131px;top:3080px;width:200px"><h4>Competitive Pricing</h4><p>Lorem ipsum dolor sit amet, consectetur adipiscing</p></div>
<div class="why" style="left:876px;top:2819px;width:220px"><h4>Customized Solutions</h4><p>Lorem ipsum dolor sit amet, consectetur adipiscing</p></div>
<div class="why" style="left:899px;top:2955px;width:200px"><h4>High-Quality</h4><p>Lorem ipsum dolor sit amet, consectetur adipiscing</p></div>
<div class="why" style="left:876px;top:3080px;width:200px"><h4>Attention to Detail</h4><p>Lorem ipsum dolor sit amet, consectetur adipiscing</p></div>

<!-- Testimonials -->
<div class="abs" style="left:0;top:3249px;width:1200px;height:535px;background:var(--testi)"></div>
<div class="label" style="left:563px;top:3306px">Testimonials</div>
<h2 class="abs" style="left:0;top:3342px;width:1200px;text-align:center;color:#fff;font-weight:500;font-size:40px">What Clients are Saying</h2>
<div class="tcard" style="left:92px"><div class="q">”</div><p>Lorem ipsum dolor sit amet, consectetur adipiscing elit, sed do eiusmod tempor i ncididunt ut labore et dolore magna aliq ua. Ut enim ad minim veniam, quis nostr</p><div class="who"><div class="av" role="img" aria-label="Client portrait"></div><div class="nm">Maren T.<small>Country</small></div></div></div>
<div class="tcard" style="left:439px"><div class="q">”</div><p>Lorem ipsum dolor sit amet, consectetur adipiscing elit, sed do eiusmod tempor i ncididunt ut labore et dolore magna aliq ua. Ut enim ad minim veniam, quis nostr</p><div class="who"><div class="av" role="img" aria-label="Client portrait"></div><div class="nm">Maren T.<small>Country</small></div></div></div>
<div class="tcard" style="left:786px"><div class="q">”</div><p>Lorem ipsum dolor sit amet, consectetur adipiscing elit, sed do eiusmod tempor i ncididunt ut labore et dolore magna aliq ua. Ut enim ad minim veniam, quis nostr</p><div class="who"><div class="av" role="img" aria-label="Client portrait"></div><div class="nm">Maren T.<small>Country</small></div></div></div>
<svg class="abs" style="left:560px;top:3703px" width="80" height="16" viewBox="0 0 80 16"><circle cx="9" cy="8" r="3" fill="#9fb1c9"/><circle cx="24" cy="8" r="3" fill="#9fb1c9"/><circle cx="40" cy="8" r="5.5" fill="none" stroke="#9fb1c9" stroke-width="1.5"/><circle cx="40" cy="8" r="2.5" fill="#9fb1c9"/><circle cx="56" cy="8" r="3" fill="#9fb1c9"/><circle cx="71" cy="8" r="3" fill="#9fb1c9"/></svg>

<!-- Contact -->
<h2 class="sec-title" style="left:103px;top:3896px;font-size:43px">Contact Us Today</h2>
<div class="citem" style="top:3975px;left:106px"><svg width="50" height="44" viewBox="0 0 50 44"><circle cx="18" cy="24" r="16" fill="#e7eef7"/><path d="M14 8h6l3 7-4 2a15 15 0 0 0 8 8l2-4 7 3v6a3 3 0 0 1-3 3A24 24 0 0 1 11 11a3 3 0 0 1 3-3z" fill="none" stroke="#1f3f75" stroke-width="1.6"/></svg><div><b>HEAD OFFICE</b><span>21 Lorem Ipsum, ABC 123</span></div></div>
<div class="citem" style="top:4048px;left:106px"><svg width="50" height="44" viewBox="0 0 50 44"><circle cx="18" cy="24" r="16" fill="#e7eef7"/><rect x="8" y="12" width="30" height="22" fill="none" stroke="#1f3f75" stroke-width="1.6"/><path d="M8 12l15 12 15-12" fill="none" stroke="#1f3f75" stroke-width="1.6"/></svg><div><b>EMAIL ADDRESS</b><span>sales@tidemill.example</span></div></div>
<div class="citem" style="top:4113px;left:106px"><svg width="50" height="44" viewBox="0 0 50 44"><circle cx="18" cy="26" r="16" fill="#e7eef7"/><path d="M24 40S12 27 12 18a12 12 0 0 1 24 0c0 9-12 22-12 22z" fill="none" stroke="#1f3f75" stroke-width="1.6"/><circle cx="24" cy="18" r="4" fill="none" stroke="#1f3f75" stroke-width="1.6"/></svg><div><b>CALL US NOW</b><span>Call Now: 555-010-240</span></div></div>

<!-- Footer -->
<svg class="abs" style="left:0;top:4270px" width="1200" height="484" viewBox="0 0 1200 484"><polygon points="0,158 388,5 1200,160 1200,484 0,484" fill="var(--navy-deep)"/><polyline points="0,160 388,5 1200,160" fill="none" stroke="#2fb3e3" stroke-width="8"/></svg>

<div class="abs" style="left:596px;top:3895px;width:495px;height:572px;background:#fff;border-top:4px solid #9aa6bd"></div>
<div class="abs head" style="left:634px;top:3946px;font-size:24px;font-weight:500;color:var(--ink)">Send Us A Message</div>
<div class="flabel" style="left:635px;top:4012px">First Name</div>
<div class="flabel" style="left:847px;top:4012px">Last Name</div>
<div class="field" style="left:635px;top:4032px;width:199px;height:42px">John</div>
<div class="field" style="left:847px;top:4032px;width:200px;height:42px">Doe</div>
<div class="flabel" style="left:635px;top:4097px">Email</div>
<div class="field" style="left:635px;top:4118px;width:418px;height:43px">office@tidemill.example</div>
<div class="flabel" style="left:635px;top:4189px">Message</div>
<div class="field" style="left:635px;top:4209px;width:418px;height:124px;border-radius:0;align-items:flex-start;padding-top:20px">Type Your Message</div>
<div class="btn" style="left:635px;top:4371px;width:155px;height:45px">Contact us
  <svg width="18" height="12" viewBox="0 0 18 12"><path d="M0 6h16M11 1l5 5-5 5" stroke="#fff" stroke-width="1.6" fill="none"/></svg></div>

<div class="foot-brand"><i style="width:20px;height:20px;background:#fff;display:block"></i><span>TideMill<br>Coatings</span></div>
<div class="fcontact" style="left:430px"><svg width="30" height="30" viewBox="0 0 30 30"><circle cx="15" cy="15" r="13" fill="none" stroke="#fff" stroke-width="1.5"/><path d="M2 15h26M15 2c-6 7-6 19 0 26M15 2c6 7 6 19 0 26" fill="none" stroke="#fff" stroke-width="1.3"/></svg><div>123, Building Name, Street<br>City, State XY 123456</div></div>
<div class="fcontact" style="left:687px"><svg width="24" height="30" viewBox="0 0 24 30"><rect x="4" y="2" width="16" height="26" rx="2" fill="none" stroke="#fff" stroke-width="1.5"/><circle cx="12" cy="23" r="1.5" fill="#fff"/></svg><div>PHONE<br>(555) 010 2400</div></div>
<div class="fcontact" style="left:864px"><svg width="28" height="30" viewBox="0 0 28 30"><rect x="2" y="7" width="24" height="17" fill="none" stroke="#fff" stroke-width="1.5"/><path d="M2 7l12 9 12-9" fill="none" stroke="#fff" stroke-width="1.5"/></svg><div>EMAIL<br>office@tidemill.example</div></div>
<div class="abs" style="left:675px;top:4536px;width:1px;height:44px;background:#51699a"></div>
<div class="abs" style="left:850px;top:4536px;width:1px;height:44px;background:#51699a"></div>
<div class="abs" style="left:258px;top:4606px;width:705px;height:1px;background:#51699a"></div>
<div class="foot-nav">
  <a style="left:276px">HOME</a><a style="left:370px">SERVICES</a><a style="left:476px">ABOUT US</a><a style="left:594px">TESTIMONIALS</a><a style="left:744px">BLOG</a><a style="left:838px">CONTACT US</a>
</div>
<div class="fsq" style="left:932px"><i></i></div><div class="fsq" style="left:966px"><i></i></div><div class="fsq" style="left:1000px"><i></i></div><div class="fsq" style="left:1034px"><i></i></div>

</body>
</html>
```